Box Packaging Design for Yoga Foam Roller

We need a box packaging design for our yoga foam roller.

1. dimensions of box: 31x16x16cm. see template.jpg for design layout & measurements. box example shows an example product & box dimensions.

2. the design style should have an organic, earth-friendly touch to it with natural colors. reference design.jpg shows the exact design style

3. please generally use wavy lines for the edges instead of sharp straight lines.

4. its a 2 color print design: light brown (see reference design) and charcoal dark blue. the "3rd color" is the brown carton base color.

5. schematic drawing.jpg shows a general blueprint for the packaging design and the placement of the elements.

6. please include yoga person from yoga silhouette.jpg and logo from logo.jpg like shown in the schematic drawing

7. please include barcode label.pdf as shown in the schematic drawing

Target Market(s)

We are a young company from Germany selling yoga and sports products in Europe. Our main markets are Germany, UK, France, Italy and Spain. For our latest product, a Yoga Foam Roller.

The target audience are people which are into Yoga, Health, Pilates, Sports and Fitness. The roller can be used to massage tissues and muscles or for a pre-workout warmup program.

Requirements
Must have
• - design style like reference design.jpg
• - dimensions according to template.jpg
• - barcode label
• - "Desigend in Germany"
• - "Made in China"
• - "Quiet Harbor" & logo according to project description, "Faszienrolle", "schwarz/blau"
• - two color design (carton background = "3rd color")
Nice to have
• - see project description (wavy lines, yoga person silhouette, ...)
• - "100% Satisfaction Guarantee" label
• - "Money Back Guarantee" label

```html
<!DOCTYPE html>
<html lang="de">
<head>
<meta charset="utf-8">
<title>Quiet Harbor – Faszienrolle Verpackung</title>
<link rel="stylesheet" href="https://fonts.googleapis.com/css2?family=Bebas+Neue&family=Dancing+Script:wght@600&family=Righteous&family=Roboto+Condensed:wght@400;700&display=swap">
<style>
  :root {
    --kraft: #c9a169;
    --kraft-dark: #b88f58;
    --paper: #eee5dd;
    --gold: #c8a06b;
    --gold-light: #d9b98a;
    --navy: #2d4357;
    --navy-deep: #1e3246;
    --mist: #a9b8c8;
    --stage: #ffffff;
  }
  * { margin: 0; padding: 0; box-sizing: border-box; }
  html, body {
    width: 1054px; height: 1200px; overflow: hidden;
    background: var(--stage);
  }
  .dieline {
    position: relative; width: 1054px; height: 1200px;
    display: flex; justify-content: center; align-items: center; gap: 0;
  }
  .panel { position: relative; width: 516px; height: 1000px; overflow: hidden; }

  /* side panel */
  .panel--side {
    background: linear-gradient(180deg, var(--kraft) 0%, var(--kraft-dark) 100%);
  }
  .info-label {
    position: absolute; left: 77px; top: 390px; width: 356px; height: 160px;
    background: var(--navy-deep); padding: 7px;
  }
  .info-label__frame {
    width: 100%; height: 100%; border: 2px solid var(--gold);
    padding: 8px 10px; color: var(--gold-light);
    font-family: "Roboto Condensed", sans-serif; font-size: 11.5px; line-height: 1.45;
  }
  .info-label__lang { font-weight: 700; font-size: 12px; margin-bottom: 3px; }
  .info-label__list { list-style: none; }
  .info-label__list li::before { content: "★"; font-size: 8px; margin-right: 3px; vertical-align: 1px; }

  /* front panel */
  .panel--front { background: var(--paper); }
  .brand-name {
    position: absolute; top: 168px; left: 0; width: 100%; text-align: center;
    font-family: "Dancing Script", cursive; font-weight: 600; font-size: 52px;
    color: var(--gold);
  }
  .product-title {
    position: absolute; top: 262px; left: 0; width: 100%; text-align: center;
    font-family: "Righteous", sans-serif; font-size: 74px; color: var(--navy);
    letter-spacing: -1px;
  }
  .product-variant {
    position: absolute; top: 346px; left: 0; width: 100%;
    display: flex; justify-content: center; align-items: center; gap: 8px;
    font-family: "Dancing Script", cursive; font-weight: 600; font-size: 28px; color: var(--navy);
  }
  .product-variant__rule { width: 46px; height: 1.5px; background: var(--navy); }
  .yoga-figure {
    position: absolute; left: 60px; top: 360px; width: 400px; height: 400px;
    background: radial-gradient(ellipse 45% 55% at 50% 55%, var(--navy) 0%, rgba(45,67,87,.75) 30%, rgba(169,184,200,.55) 60%, rgba(238,229,221,0) 100%);
  }
  .waves { position: absolute; left: 0; top: 600px; width: 516px; height: 400px; }
  .product-claim {
    position: absolute; left: 30px; bottom: 58px;
    display: flex; align-items: flex-end; gap: 8px;
    transform: rotate(-4deg); transform-origin: left bottom;
  }
  .product-claim__name {
    font-family: "Bebas Neue", sans-serif; font-size: 58px; line-height: 1; color: var(--navy-deep);
    letter-spacing: 1px;
  }
  .product-claim__love {
    font-family: "Dancing Script", cursive; font-weight: 600; font-size: 26px; line-height: .9;
    color: var(--navy-deep); padding-bottom: 18px;
  }
  .product-claim__love small { display: block; font-size: 14px; font-family: "Roboto Condensed", sans-serif; }
</style>
</head>
<body>
<main class="dieline">
  <section class="panel panel--side" aria-label="Seitenfläche">
    <div class="info-label">
      <div class="info-label__frame">
        <p class="info-label__lang">DE</p>
        <ul class="info-label__list">
          <li>Lorem ipsum dolor sit amet, consectetur adipiscing Elit.</li>
          <li>Produktion af frygt er altid af den største.</li>
          <li>Lorem ipsum dolor sit amet, consectetur adipiscing Elit.</li>
          <li>Produktion af frygt er altid af den største.</li>
          <li>Lorem ipsum dolor sit amet, consectetur adipiscing Elit.</li>
          <li>Produktion af frygt er altid af den største.</li>
        </ul>
      </div>
    </div>
  </section>

  <section class="panel panel--front" aria-label="Vorderseite">
    <p class="brand-name">Quiet Harbor</p>
    <h1 class="product-title">Faszienrolle</h1>
    <p class="product-variant">
      <span class="product-variant__rule"></span>Schwarz/blau<span class="product-variant__rule"></span>
    </p>
    <div class="yoga-figure" role="img" aria-label="Silhouette einer meditierenden Person im Lotussitz vor einer angedeuteten Lotusblüte"></div>
    <svg class="waves" viewBox="0 0 516 400" aria-hidden="true">
      <path d="M0 250 C120 200 260 120 516 40 L516 400 L0 400 Z" fill="var(--gold-light)" opacity=".55"/>
      <path d="M0 270 C140 215 290 140 516 80" fill="none" stroke="var(--paper)" stroke-width="9"/>
      <path d="M0 300 C150 240 300 160 516 110 L516 400 L0 400 Z" fill="var(--gold)" opacity=".7"/>
      <path d="M0 318 C160 260 320 190 516 150" fill="none" stroke="var(--paper)" stroke-width="7"/>
      <path d="M0 340 C170 290 330 220 516 190 L516 400 L0 400 Z" fill="var(--gold)"/>
    </svg>
    <div class="product-claim">
      <span class="product-claim__name">Yoga Foam Roller</span>
      <span class="product-claim__love">With<small>100%</small>Love</span>
    </div>
  </section>
</main>
</body>
</html>
```